New Label Design Project

I need a coffee label that i can edit based on the designs we first came up with. The coffee bags i will use are 250g side gusseted Matt black so it can capture the colours in the logos.. My issue is that i need to add information regarding the type of coffee I am selling - Im using 5 single origin sourced coffee and the beans are all 100% arabica and ill add some information on the current stock I’m using… Im out of ideas at the moment! but want to keep it clean and fresh… Information I must have is weight… 250g and roasted on date (best used within 3 months of date). anything else will be considered?! Ill attached the logos / references and also the website which is still under development… www.tqcoffee.co.uk

```html
<!DOCTYPE html>
<html lang="en">
<head>
<meta charset="utf-8">
<title>Tidequay Roastery Coffee – Bag Labels</title>
<link href="https://fonts.googleapis.com/css2?family=Rye&family=Roboto+Condensed:wght@400;700&family=Damion&family=Libre+Baskerville:ital@1&display=swap" rel="stylesheet">
<style>
  :root {
    --canvas: #f9e18e;
    --ink: #1b1a19;
    --panel: #221e1a;
    --copper: #b9773a;
    --copper-dark: #8d5a2b;
    --cream: #ece3cf;
    --illustration: #5c5650;
  }
  * { margin: 0; padding: 0; box-sizing: border-box; }
  html, body { width: 1200px; height: 1200px; overflow: hidden; }
  body {
    position: relative;
    background: var(--canvas);
    font-family: "Roboto Condensed", "Arial Narrow", sans-serif;
  }

  /* Brand band */
  .brand-band {
    position: absolute; left: 0; top: 56px;
    width: 1200px; height: 204px;
    background: var(--ink);
  }
  .brand-lockup {
    position: absolute; left: 362px; top: 29px;
    width: 476px; height: 138px;
    background: var(--panel);
    display: flex; align-items: center;
    color: var(--cream);
  }
  .brand-dot {
    width: 44px; height: 44px; border-radius: 50%;
    background: var(--cream);
    margin-left: 46px;
  }
  .brand-divider {
    width: 2px; height: 92px; background: var(--copper);
    margin: 0 30px 0 36px;
  }
  .brand-words { display: flex; flex-direction: column; align-items: center; }
  .brand-name {
    font-family: "Rye", serif; font-size: 44px; letter-spacing: 2px; line-height: 1;
  }
  .brand-sub {
    font-family: "Rye", serif; font-size: 16px; letter-spacing: 4px; margin-top: 12px;
  }

  /* Bags */
  .bag {
    position: absolute;
    background: var(--ink);
    border-radius: 14px 14px 8px 8px;
    overflow: hidden;
    color: var(--cream);
  }
  .bag-front { left: 125px; top: 338px; width: 400px; height: 638px; }
  .bag-back  { left: 650px; top: 346px; width: 418px; height: 640px; }
  .bag-seal {
    position: absolute; left: 0; top: 14px; width: 100%; height: 64px;
    background: linear-gradient(180deg, var(--copper) 0%, var(--copper-dark) 100%);
  }
  .bag-seal::after {
    content: ""; position: absolute; left: 0; bottom: 6px; width: 100%; height: 2px;
    background: var(--ink); opacity: .6;
  }

  /* Front face */
  .badge {
    position: absolute; left: 50%; top: 182px; transform: translateX(-50%);
    width: 240px; height: 240px; border-radius: 50%;
    border: 4px solid var(--copper);
    display: flex; flex-direction: column; align-items: center; justify-content: center;
  }
  .badge-name {
    font-family: "Rye", serif; font-size: 34px; color: var(--copper); letter-spacing: 1px;
  }
  .badge-place {
    font-family: "Rye", serif; font-size: 16px; color: var(--cream); letter-spacing: 3px; margin-top: 14px;
  }
  .badge-year {
    font-family: "Rye", serif; font-size: 13px; color: var(--cream); letter-spacing: 3px; margin-top: 4px;
  }
  .front-tagline {
    position: absolute; top: 478px; width: 100%; text-align: center;
    font-family: "Damion", cursive; font-size: 36px; color: var(--copper);
  }
  .front-variety {
    position: absolute; top: 528px; width: 100%; text-align: center;
    font-size: 24px; color: var(--copper); letter-spacing: .5px;
  }
  .front-weight {
    position: absolute; right: 14px; bottom: 28px;
    font-size: 17px; font-weight: 700; color: var(--copper);
  }

  /* Back face */
  .location-arc {
    position: absolute; left: 0; top: 0;
  }
  .lighthouse-art {
    position: absolute; left: 50%; top: 264px; transform: translateX(-50%);
    width: 44px; height: 144px;
    background: linear-gradient(180deg, var(--cream) 0%, var(--illustration) 100%);
  }
  .estd {
    position: absolute; top: 352px; font-family: "Rye", serif; font-size: 12px;
    color: var(--copper); letter-spacing: 2px; padding: 3px 0;
    border-top: 1px solid var(--copper); border-bottom: 1px solid var(--copper);
  }
  .estd-left { left: 118px; }
  .estd-right { right: 118px; }
  .back-name {
    position: absolute; top: 420px; width: 100%; text-align: center;
    font-family: "Rye", serif; font-size: 40px; letter-spacing: 2px; color: var(--cream);
  }
  .back-sub {
    position: absolute; top: 474px; width: 100%; text-align: center;
    font-family: "Rye", serif; font-size: 15px; letter-spacing: 3px; color: var(--copper);
  }
  .back-note {
    position: absolute; top: 508px; width: 100%; text-align: center;
    font-family: "Libre Baskerville", serif; font-style: italic; font-size: 11px; color: var(--copper);
  }
  .back-dates {
    position: absolute; top: 594px; width: 100%; text-align: center;
    font-size: 12px; line-height: 1.45; color: var(--copper);
  }
</style>
</head>
<body>

  <header class="brand-band">
    <div class="brand-lockup">
      <span class="brand-dot"></span>
      <span class="brand-divider"></span>
      <div class="brand-words">
        <span class="brand-name">TIDEQUAY</span>
        <span class="brand-sub">ROASTERY COFFEE</span>
      </div>
    </div>
  </header>

  <section class="bag bag-front">
    <div class="bag-seal"></div>
    <div class="badge">
      <span class="badge-name">TIDEQUAY</span>
      <span class="badge-place">SALTMERE</span>
      <span class="badge-year">ESTD 2018</span>
    </div>
    <p class="front-tagline">- Coffee and the Beans -</p>
    <p class="front-variety">100% Arabica</p>
    <p class="front-weight">Net wet. 250g</p>
  </section>

  <section class="bag bag-back">
    <div class="bag-seal"></div>
    <svg class="location-arc" width="418" height="400" viewBox="0 0 418 400">
      <defs><path id="locationPath" d="M 99 322 A 120 120 0 0 1 319 322"/></defs>
      <text font-family="Roboto Condensed, sans-serif" font-size="11" letter-spacing="1.4" fill="#b9773a">
        <textPath href="#locationPath" startOffset="50%" text-anchor="middle">SALTMERE, COAST COUNTY, UNITED KINGDOM</textPath>
      </text>
    </svg>
    <div class="lighthouse-art" role="img" aria-label="Illustration of a striped lighthouse"></div>
    <span class="estd estd-left">ESTD</span>
    <span class="estd estd-right">2018</span>
    <p class="back-name">TIDEQUAY</p>
    <p class="back-sub">ROASTERY COFFEE</p>
    <p class="back-note">Best used within 3 months of date</p>
    <p class="back-dates">Manufacured in January 1, 2019<br>Expires on April 1, 2019</p>
  </section>

</body>
</html>
```